Digitale Weihnachtskarte für Energieberater
Zielgruppe
Beratung in Bezug auf Energiemanagement/Energieeffizienz in Gebäuden
Gebäudetechnik
Kunden aufzeigen, wie Energie und somit Kosten gespart werden können
Zielgruppe: unsere Kunden, Interessenten und Lieferanten
Aufgabenstellung
Die digitale Weihnachtskarte wird schlussendlich per Mailing verschickt. Es wird eine jpg- und eine pdf-Datei benötigt.
Design:
Weihnachtliches, eher schlichtes Design. Letztjährige Projekte: #293721, #484192, #437447
Logo muss integriert werden, muss aber nicht im Vordergrund stehen.
Das Bild im Anhang kann, aber muss nicht verwendet werden.
Farbwahl:
Blau:
CMYK = 95/75/0/0
HEX = #244a9a
RGB = 36/74/154
Orange:
CMYK = 0/60/100/0
HEX = #ef7d00
RGB = 239/125/0
Grau:
CMYK = 0/0/0/65
HEX = #7c7c7b
RGB = 124/124/123
Grün:
CMYK = 60/100/0/0
HEX = #76b82a
RGB = 118/184/42
Schrift: DIN oder Arial, nicht kursiv
Geschätzte Kunden und Partner
Das Jahr neigt sich dem Ende zu und lädt uns dazu ein, auf das vergangene Jahr zurückzublicken, aber auch mit Zuversicht und frischem Elan in einen neuen Zeitabschnitt zu starten. Dank fortschrittlichen Technologien, Prozessoptimierungen und Investitionen wurde der Erfolg der vendralis Schweiz AG vorangetrieben. Mit unserem neuen Standort in Stuttgart haben wir einen weiteren Meilenstein gelegt.
Dankbar dafür, dass wir mit Ihnen zusammen in die Zukunft weiterschreiten dürfen, wünschen wir Ihnen und Ihrer Familie eine entspannte und besinnliche Weihnachtszeit und ein glückliches neues Jahr!

```html
<!DOCTYPE html>
<html lang="de">
<head>
<meta charset="utf-8">
<title>vendralis – Weihnachtskarte</title>
<link rel="stylesheet" href="https://fonts.googleapis.com/css2?family=Arimo:wght@400&family=Pinyon+Script&display=swap">
<style>
  :root {
    --page-bg: #e4e4e4;
    --card-bg: #ffffff;
    --brand-blue: #244a9a;
    --night-deep: #07072a;
    --night-mid: #10206a;
    --glow-blue: #2f7de0;
    --glow-core: #bfe6ff;
    --dusk-red: #5a2a4a;
    --script-white: #ffffff;
  }
  * { box-sizing: border-box; margin: 0; padding: 0; }
  html, body {
    width: 1200px; height: 1200px; overflow: hidden;
    background: var(--page-bg);
  }
  .card {
    position: absolute; left: 128px; top: 86px;
    width: 942px; height: 975px;
    background: var(--card-bg);
    box-shadow: 0 1px 4px rgba(0,0,0,0.18);
    display: flex;
  }
  .card-visual {
    position: relative; width: 507px; height: 100%;
    background:
      radial-gradient(ellipse 55% 30% at 52% 54%, var(--glow-core) 0%, rgba(80,170,255,0.75) 18%, rgba(40,110,230,0) 60%),
      radial-gradient(ellipse 120% 60% at 50% 85%, rgba(40,120,230,0.85) 0%, rgba(20,60,160,0.6) 45%, rgba(16,32,106,0) 75%),
      radial-gradient(ellipse 70% 40% at 100% 100%, rgba(90,42,74,0.9), rgba(90,42,74,0) 70%),
      linear-gradient(180deg, var(--night-deep) 0%, var(--night-mid) 35%, #1a4fb4 60%, #14307a 100%);
  }
  .greeting {
    position: absolute; left: 0; top: 0; width: 100%;
    font-family: "Pinyon Script", cursive;
    color: var(--script-white);
    text-shadow: 0 0 6px rgba(0,0,0,0.4);
    line-height: 1;
  }
  .greeting span { position: absolute; white-space: nowrap; }
  .greeting .g-frohe { left: 155px; top: 140px; font-size: 64px; }
  .greeting .g-weihnachten { left: 80px; top: 228px; font-size: 64px; }
  .greeting .g-gutes { left: 183px; top: 300px; font-size: 40px; }
  .greeting .g-jahr { left: 165px; top: 350px; font-size: 40px; }

  .card-message {
    position: relative; flex: 1;
    font-family: Arimo, Arial, sans-serif;
    color: var(--brand-blue);
  }
  .brand {
    position: absolute; left: 50px; top: 96px;
    display: flex; align-items: center; gap: 12px;
    font-size: 38px; letter-spacing: 0.5px;
  }
  .brand-dot {
    width: 40px; height: 40px; border-radius: 50%;
    background: var(--brand-blue);
  }
  .letter {
    position: absolute; left: 48px; top: 226px; width: 380px;
    font-size: 19px; line-height: 24px;
  }
  .letter p + p { margin-top: 24px; }
  .site {
    position: absolute; left: 42px; top: 850px;
    font-size: 11px;
  }
  .rule {
    position: absolute; left: 42px; top: 879px; width: 363px;
    border-top: 1px solid var(--brand-blue);
  }
  .offices {
    position: absolute; left: 42px; top: 900px;
    display: flex; gap: 0;
    font-size: 11px; line-height: 13.5px;
    font-style: normal;
  }
  .office { width: 181px; }
  .office + .office { width: 200px; }
</style>
</head>
<body>
  <main class="card">
    <section class="card-visual" role="img" aria-label="Winterliche Nachtillustration: leuchtende blaue Erdkugel mit Lichtnetz und Schneeflocken">
      <h1 class="greeting">
        <span class="g-frohe">Frohe</span>
        <span class="g-weihnachten">Weihnachten</span>
        <span class="g-gutes">und ein gutes</span>
        <span class="g-jahr">Neues Jahr</span>
      </h1>
    </section>

    <section class="card-message">
      <div class="brand"><span class="brand-name">vendralis</span><span class="brand-dot"></span></div>

      <div class="letter">
        <p>Geschätzte Kunden und Partner</p>
        <p>Das Jahr neigt sich dem Ende zu und<br>lädt uns dazu ein, auf das vergangene<br>Jahr zurückzublicken, aber auch mit<br>Zuversicht und frischem Elan in einen<br>neuen Zeitabschnitt zu starten. Dank<br>fortschrittlichen Technologien, Prozes-<br>soptimierungen und Investitionen<br>wurde der Erfolg der vendralis Schweiz<br>AG vorangetrieben. Mit unserem neuen<br>Standort in Stuttgart haben wir einen<br>weiteren Meilenstein gelegt.</p>
        <p>Dankbar dafür, dass wir mit Ihnen<br>zusammen in die Zukunft weiterschreit-<br>en dürfen, wünschen wir Ihnen und<br>Ihrer Familie eine entspannte und be-<br>sinnliche Weihnachtszeit und ein glück-<br>liches neues Jahr!</p>
        <p>Ihr vendralis-Team</p>
      </div>

      <div class="site">www.vendralis.com</div>
      <div class="rule"></div>
      <address class="offices">
        <div class="office">vendralis Schweiz AG<br>Talstrasse 19<br>4600 Olten<br>Tel. +41 62 000 12 34</div>
        <div class="office">vendralis Schweiz AG<br>Niederlassung Deutschland<br>Werkstrasse 9, 70565 Stuttgart<br>Tel. +49 711 00000 210</div>
      </address>
    </section>
  </main>
</body>
</html>
```